Lumi-Leaf Label for the Tea Tins and Boxes

We need a label design for our tea company. Our company promotes natural beauty from the inside out. We have many single and blended tea's that target specific markets, ie. weight loss, anti aging, healthy skin/hair etc. I want this design to attract ages 21 to 65. We need the label to be a white background with colour and black accents. We would like the use of herbs as the background.

Target Market(s)

attract ages 21 to 65. .

Industry/Entity Type

It Company

Font styles to use
Serif
Decorative

Colors
f78f20
ffffff
9bcb3c
0792cd
fbed22

Requirements
Must have
• we must have a clean design
Nice to have
• Color with black accents
Should not have
• busy design

```html
<!DOCTYPE html>
<html lang="en">
<head>
<meta charset="utf-8">
<title>Lumi-Leaf Key Lime Cold Brew Label</title>
<link rel="stylesheet" href="https://fonts.googleapis.com/css2?family=Rye&family=Old+Standard+TT:wght@400;700&family=Oswald:wght@400;500&display=swap">
<style>
  :root {
    --paper: #ffffff;
    --herb-green: #5f8420;
    --herb-light: #e4ecd3;
    --herb-mid: #b8cc8e;
    --ink: #1a1a1a;
    --backdrop: #ffffff;
  }
  * { box-sizing: border-box; margin: 0; padding: 0; }
  html, body {
    width: 1200px; height: 1200px; overflow: hidden;
    background: var(--backdrop);
  }
  .label {
    position: absolute; left: 180px; top: 60px;
    width: 840px; height: 1080px;
    background: var(--paper);
  }
  .herb-backdrop {
    position: absolute; inset: 0;
    background:
      radial-gradient(ellipse at 15% 20%, var(--herb-mid) 0%, transparent 45%),
      radial-gradient(ellipse at 85% 80%, var(--herb-mid) 0%, transparent 45%),
      radial-gradient(ellipse at 10% 85%, #9fb86a 0%, transparent 40%),
      linear-gradient(160deg, var(--herb-light), #d3e0b6 50%, var(--herb-light));
  }
  .info-panel {
    position: absolute; left: 171px; top: 105px;
    width: 553px; height: 890px;
    background: var(--paper);
    border: 9px solid var(--herb-green);
  }
  .info-panel::before {
    content: ""; position: absolute; inset: 10px;
    border: 3px dotted var(--ink);
  }
  .line { position: absolute; left: 0; right: 0; text-align: center; }
  .brand {
    top: 140px; font-family: "Old Standard TT", serif; font-weight: 700;
    font-size: 28px; color: var(--ink); letter-spacing: 1px;
    display: flex; justify-content: center; align-items: center; gap: 10px;
  }
  .brand .dot { width: 12px; height: 12px; border-radius: 50%; background: var(--ink); }
  .flavour {
    top: 285px; font-family: "Rye", serif; font-size: 86px;
    color: var(--ink); line-height: 1;
  }
  .style {
    top: 410px; font-family: "Old Standard TT", serif; font-size: 30px;
    letter-spacing: 16px; color: var(--ink); padding-left: 16px;
  }
  .details {
    top: 555px; font-family: "Old Standard TT", serif; font-weight: 700;
    font-size: 17px; line-height: 1.5; color: var(--ink); text-transform: uppercase;
  }
  .yield {
    top: 700px; font-family: "Oswald", sans-serif; font-weight: 500;
    font-size: 48px; color: var(--herb-green); letter-spacing: 1px;
    display: flex; justify-content: center; align-items: baseline; gap: 18px;
  }
  .yield .count { font-size: 76px; font-weight: 400; }
  .weight {
    top: 825px; font-family: "Old Standard TT", serif; font-weight: 700;
    font-size: 12px; color: var(--ink); text-transform: uppercase;
  }
</style>
</head>
<body>
  <main class="label">
    <div class="herb-backdrop" role="img" aria-label="Green line-art herbs, leaves, limes and peppercorns surrounding the label"></div>
    <section class="info-panel">
      <div class="line brand"><span>Lumi-Leaf Co.</span><span class="dot"></span></div>
      <h1 class="line flavour">KEY LIME</h1>
      <p class="line style">COLD BREW</p>
      <p class="line details">Refreshing green tea blend<br>&amp; extra large wire mesh filter</p>
      <p class="line yield"><span>BREWS</span><span class="count">3</span><span>GALLONS</span></p>
      <p class="line weight">3oz net wt (85g)</p>
    </section>
  </main>
</body>
</html>
```